need a clean, modern job advertisement designed for social media (Facebook & Instagram).

The post is to advertise two positions:
• Leading Hand Boilermaker
• Dragline Fitter
We want the design to match our KRT Plant Services branding: blue, white, strong, professional, mining-industry style.
What the design should include:
Bold headline: “WE’RE HIRING”
Sub-headline: “Leading Hand Boilermaker & Dragline Fitter”
Key points:
• Bowen Basin based
• Dragline & shovel maintenance
• Great pay + long-term work
• Locally owned & operated
KRT logo placed cleanly
Space for 1–2 images (boilermaking or dragline work)
Design style:
Strong and industrial
Blue/white colour scheme
Easy to read at a glance
Suitable for a square 1080×1080 design

```html
<!DOCTYPE html>
<html lang="en">
<head>
<meta charset="utf-8">
<title>KRT Plant Services – We're Hiring</title>
<link rel="stylesheet" href="https://fonts.googleapis.com/css2?family=Bebas+Neue&family=Roboto+Condensed:wght@500;600&display=swap">
<style>
  :root {
    --stage: #b3b3b3;
    --paper: #f2f2f2;
    --white: #ffffff;
    --ink: #0a0a0a;
    --blue-deep: #0b4fd0;
    --blue-mid: #1677ea;
    --blue-bright: #22b0f7;
    --sky: #7fb6e8;
    --sand: #d9c69c;
    --night: #141414;
    --flame: #d9541c;
  }
  * { box-sizing: border-box; margin: 0; padding: 0; }
  html, body { width: 1200px; height: 603px; overflow: hidden; background: var(--stage); }
  .post {
    position: absolute; left: 350px; top: 51px; width: 500px; height: 500px;
    background: var(--paper); overflow: hidden;
    font-family: "Roboto Condensed", "Arial Narrow", sans-serif;
  }
  .top-strip { position: absolute; left: 0; top: 0; width: 305px; height: 23px; background: var(--white); }
  .stripe-panel { position: absolute; left: 305px; top: 0; width: 195px; height: 64px; background: #e6e6e6; }
  .stripes { position: absolute; left: 23px; top: 23px; display: flex; gap: 10px; }
  .stripes span { width: 10px; height: 30px; background: var(--ink); }
  .stripes span:nth-child(odd) { background: linear-gradient(180deg, var(--blue-bright), var(--blue-deep)); }
  .hero {
    position: absolute; left: 0; top: 23px; width: 318px; height: 154px;
    background: radial-gradient(ellipse at 35% 40%, var(--blue-bright) 0%, var(--blue-mid) 45%, var(--blue-deep) 100%);
  }
  .headline { position: absolute; left: 24px; top: 22px; font-family: "Bebas Neue", "Impact", sans-serif; color: var(--white); line-height: .8; }
  .headline .line-1 { display: block; font-size: 82px; letter-spacing: -2px; transform: scaleY(1.05); transform-origin: top left; }
  .headline .line-2 { display: block; font-size: 138px; letter-spacing: -3px; margin-top: -4px; }
  .role-panel {
    position: absolute; left: 249px; top: 64px; width: 251px; height: 133px; background: var(--night);
    z-index: 0;
  }
  .hero { z-index: 1; }
  .headline { z-index: 2; }
  .role-title {
    position: absolute; left: 79px; top: 20px; color: var(--white);
    font-size: 29px; font-weight: 600; line-height: 30px; letter-spacing: -.3px;
  }
  .perks { position: absolute; left: 22px; top: 202px; list-style: none; }
  .perks li { display: flex; align-items: center; gap: 9px; height: 26px; font-size: 21px; font-weight: 500; color: var(--ink); letter-spacing: -.2px; }
  .perks svg { width: 16px; height: 16px; flex: none; }
  .brand-block {
    position: absolute; left: 298px; top: 197px; width: 202px; height: 129px; background: var(--white);
    display: flex; align-items: center; justify-content: center; gap: 8px;
  }
  .brand-mark { width: 22px; height: 22px; border-radius: 50%; background: var(--blue-mid); }
  .brand-name { font-size: 22px; font-weight: 600; color: var(--blue-deep); letter-spacing: -.2px; }
  .photo { position: absolute; top: 326px; height: 174px; }
  .photo-dragline { left: 0; width: 249px; background: linear-gradient(180deg, var(--sky) 0%, #cfe2f3 55%, #8a9a5a 72%, var(--sand) 100%); }
  .photo-welder { left: 249px; width: 251px; background: radial-gradient(ellipse at 45% 55%, var(--flame) 0%, #7a2a10 35%, var(--night) 75%); }
  .contact { position: absolute; left: 0; right: 0; top: 448px; display: flex; justify-content: center; gap: 16px; color: var(--white); font-size: 15px; font-weight: 500; }
  .contact span { display: flex; align-items: center; gap: 6px; }
  .contact svg { height: 14px; }
</style>
</head>
<body>
  <main class="post">
    <div class="top-strip"></div>
    <div class="stripe-panel">
      <div class="stripes"><span></span><span></span><span></span><span></span><span></span><span></span><span></span><span></span></div>
    </div>
    <div class="role-panel">
      <p class="role-title">Leading Hand<br>Boilermaker &amp;<br>Dragline Fitter</p>
    </div>
    <div class="hero"></div>
    <h1 class="headline"><span class="line-1">WE’RE</span><span class="line-2">HIRING</span></h1>

    <ul class="perks">
      <li><svg viewBox="0 0 16 16"><path d="M3 1h6l6 7-6 7H3l6-7z" fill="var(--blue-bright)"/><path d="M1 4h4l4 4-4 4H1l4-4z" fill="var(--blue-deep)"/></svg>Bowen Basin based</li>
      <li><svg viewBox="0 0 16 16"><path d="M3 1h6l6 7-6 7H3l6-7z" fill="var(--blue-bright)"/><path d="M1 4h4l4 4-4 4H1l4-4z" fill="var(--blue-deep)"/></svg>Dragline &amp; shovel maintenance</li>
      <li><svg viewBox="0 0 16 16"><path d="M3 1h6l6 7-6 7H3l6-7z" fill="var(--blue-bright)"/><path d="M1 4h4l4 4-4 4H1l4-4z" fill="var(--blue-deep)"/></svg>Great pay + long-term work</li>
      <li><svg viewBox="0 0 16 16"><path d="M3 1h6l6 7-6 7H3l6-7z" fill="var(--blue-bright)"/><path d="M1 4h4l4 4-4 4H1l4-4z" fill="var(--blue-deep)"/></svg>Locally owned &amp; operated</li>
    </ul>

    <div class="brand-block">
      <span class="brand-mark"></span>
      <span class="brand-name">KRT Plant Services</span>
    </div>

    <div class="photo photo-dragline" role="img" aria-label="Dragline excavator working on a sandy mine site under a blue sky"></div>
    <div class="photo photo-welder" role="img" aria-label="Boilermaker in orange workwear welding a large steel pipe with sparks"></div>

    <div class="contact">
      <span><svg viewBox="0 0 20 14"><rect x="0.5" y="0.5" width="19" height="13" rx="1" fill="var(--blue-bright)"/><path d="M1 1l9 7 9-7" fill="none" stroke="var(--white)" stroke-width="1.4"/></svg>admin@krtplant.com.au</span>
      <span><svg viewBox="0 0 14 14"><path d="M3 1l2.5 3-1.5 1.5c.8 1.8 2.2 3.2 4 4L9.5 8 13 10.5 11.5 13C6 12.5 1.5 8 1 2.5z" fill="var(--blue-bright)"/></svg>+61 400 555 017</span>
    </div>
  </main>
</body>
</html>
```